Award winning pet photographer needs business card and letterhead

Business card and letterhead for our Pet photography business. We specialize in studio portraits of dogs.

Target Market(s)

Wealthy and middle class dog owners who would like photos of their dogs as wall art.

Industry/Entity Type

Portrait Photography

Contact Information for Business Card

Our business name is Tails of Glee Pet Photography. Would be good to include dog and a heart, bright colours and a modern design

Font styles to use
Sans Serif

Colors
f04a50
f68d4d
faa54b
33a6d7
33b8a4
abd036

Requirements
Must have
• Business name: Tails of Glee Pet Photography
• Phone number: 0437 560914
• Email: marcus@kfstudio.com.au
• Website:www.tailsofglee.com.au
• Photographer: Marcus Fenwick
Nice to have
• In Addition letterhead should include
• Studio address 27 Wren Close, Marrowdale 6015
• Postal Address 9 Harlow St, East Marrowdale 6015

```html
<!DOCTYPE html>
<html lang="en">
<head>
<meta charset="utf-8">
<title>Tails of Glee Pet Photography – Business Card</title>
<link rel="stylesheet" href="https://fonts.googleapis.com/css2?family=Questrial&family=Arimo:wght@400;700&display=swap">
<style>
  :root {
    --backdrop: #1c1c1c;
    --coral: #f04a50;
    --coral-band: #d9464e;
    --coral-stripe: #e8606a;
    --paper: #f4f4f4;
    --ink: #1f1f1f;
    --lime: #abd036;
    --white: #ffffff;
  }
  * { box-sizing: border-box; margin: 0; padding: 0; }
  html, body {
    width: 1200px; height: 800px; overflow: hidden;
    background: var(--backdrop);
  }
  .stage {
    position: relative; width: 1200px; height: 800px;
  }
  .card {
    position: absolute; width: 540px; height: 310px;
    top: 245px; overflow: hidden;
  }

  /* Front */
  .card-front {
    left: 40px; background: var(--coral);
    display: flex; flex-direction: column; align-items: center; justify-content: center;
  }
  .front-mark {
    width: 110px; height: 110px; border-radius: 50%;
    background: var(--white); margin-bottom: 18px;
  }
  .front-name {
    font-family: "Questrial", sans-serif; font-weight: 400;
    color: var(--white); text-align: center; line-height: 1.05;
    font-size: 38px; letter-spacing: 0.5px;
  }
  .front-name .sub { display: block; font-size: 26px; }

  /* Back */
  .card-back { left: 620px; background: var(--paper); }
  .back-brand {
    position: absolute; left: 44px; top: 34px;
    display: flex; align-items: center; gap: 10px;
  }
  .back-brand-mark {
    width: 34px; height: 34px; border-radius: 50%; background: var(--coral);
  }
  .back-brand-name {
    font-family: "Questrial", sans-serif; font-weight: 400;
    color: var(--coral); font-size: 17px; line-height: 1.1;
  }
  .back-person {
    position: absolute; right: 40px; top: 100px; text-align: right;
    font-family: "Arimo", sans-serif;
  }
  .person-name { color: var(--coral); font-weight: 700; font-size: 16px; }
  .person-role { color: var(--ink); font-size: 13px; margin-top: 3px; }
  .stripe {
    position: absolute; left: 0; right: 0; top: 148px; height: 11px;
    background: var(--coral-stripe);
  }
  .contact {
    position: absolute; left: 0; right: 0; top: 170px;
    font-family: "Arimo", sans-serif; font-size: 13px; color: var(--ink);
    text-align: center; line-height: 17px;
  }
  .web-band {
    position: absolute; left: 0; right: 0; top: 250px; height: 30px;
    background: var(--coral-band);
    font-family: "Arimo", sans-serif; font-size: 15px; color: var(--white);
    display: flex; align-items: center; justify-content: center;
  }
</style>
</head>
<body>
<main class="stage">
  <section class="card card-front">
    <div class="front-mark"></div>
    <p class="front-name">TAILS OF GLEE<span class="sub">pet photography</span></p>
  </section>

  <section class="card card-back">
    <div class="back-brand">
      <div class="back-brand-mark"></div>
      <p class="back-brand-name">Tails of Glee<br>Pet Photography</p>
    </div>
    <div class="back-person">
      <p class="person-name">Marcus Fenwick</p>
      <p class="person-role">Photographer</p>
    </div>
    <div class="stripe"></div>
    <div class="contact">
      <p>0437 560914</p>
      <p>marcus@kfstudio.com.au</p>
      <p>Studio address: 27 Wren Close, Marrowdale 6015</p>
      <p>Postal Address: 9 Harlow St, East Marrowdale 6015</p>
    </div>
    <div class="web-band">www.tailsofglee.com.au</div>
  </section>
</main>
</body>
</html>
```